Business Card Design for BrightlaneReach.com

--I need a business card design for my company BrightlaneReach.com

I have attached my logo...I want the brightlane reach logo on the front of the business card, and then I want The Brightlane Chief on the back of it with my information.

I would like to see a light colored background as well as a dark colored background

FRONT:
BRIGHTLANE REACH LOGO
247 E. Pelham Row
5th Floor
San Diego CA 92384
www.BrightlaneReach.com

Advanced Website & App Development
Websites, Apps, Online Voucher Systems

Leading Edge Marketing Services
SMS, VB, SMM, SEM,

BACK:
BRIGHTLANE CHIEF LOGO
Dorian Welker
The Brightlane Chief
Call Or Text: 555-204-3378
Dorian@BrightlaneChief.com
www.BrightlaneChief.com

Target Market(s)

small business owners

Industry/Entity Type

Business Consultant

Contact Information for Business Card

FRONT:
BRIGHTLANE REACH LOGO
247 E. Pelham Row
5th Floor
San Diego CA 92384
www.BrightlaneReach.com

SMS, VB, SMM, SEM,

BACK:
BRIGHTLANE CHIEF LOGO
Dorian Welker
The Brightlane Chief
Dorian@BrightlaneChief.com
www.BrightlaneChief.com

Requirements
Must have
• add this quote on it somewhere, anywhere,preferrably on back
• "Every Bold Step Opens A Brighter Lane”
• — Dorian Welker, Brightlane Chief
Nice to have
• open
Should not have
• red

```html
<!DOCTYPE html>
<html lang="en">
<head>
<meta charset="utf-8">
<title>Brightlane Reach – Business Cards</title>
<link href="https://fonts.googleapis.com/css2?family=Questrial&family=Mulish:wght@800&display=swap" rel="stylesheet">
<style>
  :root {
    --backdrop: #2c3034;
    --card: #ffffff;
    --brand-blue: #0e72b0;
    --band-blue: #0a6fae;
    --ink-grey: #6b6e70;
    --rule-grey: #8a8d8f;
    --divider: #2b5f82;
    --web-ink: #333333;
    --white: #ffffff;
  }
  * { box-sizing: border-box; margin: 0; padding: 0; }
  html, body { width: 1200px; height: 900px; overflow: hidden; }
  body {
    background: var(--backdrop);
    font-family: "Questrial", sans-serif;
    position: relative;
  }
  .card {
    position: absolute;
    top: 295px;
    width: 540px;
    height: 310px;
    background: var(--card);
    overflow: hidden;
    box-shadow: 0 10px 24px rgba(0,0,0,.35);
  }
  .card--back { left: 40px; }
  .card--front { left: 620px; }

  /* Back card */
  .chief-logo {
    position: absolute;
    left: 30px; top: 30px;
    color: var(--brand-blue);
    font-size: 21px;
    letter-spacing: 1.5px;
    white-space: nowrap;
  }
  .person {
    position: absolute;
    right: 40px; top: 70px;
    text-align: right;
    white-space: nowrap;
  }
  .person__name {
    font-family: "Mulish", sans-serif;
    font-weight: 800;
    color: var(--brand-blue);
    font-size: 24px;
    line-height: 1.05;
  }
  .person__title {
    color: var(--ink-grey);
    font-size: 20px;
    line-height: 1.2;
  }
  .chief-rule {
    position: absolute;
    left: 30px; right: 40px; top: 134px;
    height: 2px;
    background: var(--rule-grey);
  }
  .contact-band {
    position: absolute;
    left: 0; right: 0; top: 180px;
    height: 92px;
    background: var(--band-blue);
    display: flex;
  }
  .contact-cell {
    flex: 1;
    position: relative;
    display: flex;
    align-items: center;
    justify-content: center;
    color: var(--white);
    font-size: 13px;
    padding-top: 14px;
    white-space: nowrap;
  }
  .contact-cell + .contact-cell { border-left: 2px solid var(--divider); }
  .contact-cell__icon {
    position: absolute;
    top: -17px; left: 50%;
    transform: translateX(-50%);
    width: 34px; height: 34px;
  }

  /* Front card */
  .reach-logo {
    position: absolute;
    left: 0; right: 0; top: 34px;
    text-align: center;
    color: var(--brand-blue);
    font-size: 40px;
    letter-spacing: 3px;
    white-space: nowrap;
  }
  .reach-rule {
    position: absolute;
    left: 60px; right: 60px; top: 100px;
    height: 2px;
    background: var(--rule-grey);
  }
  .tagline {
    position: absolute;
    left: 0; right: 0; top: 114px;
    text-align: center;
    color: var(--brand-blue);
    font-size: 19px;
  }
  .web {
    position: absolute;
    left: 0; right: 0; top: 160px;
    text-align: center;
    color: var(--web-ink);
    font-size: 19px;
  }
  .web__name { color: var(--brand-blue); }
  .address-band {
    position: absolute;
    left: 0; right: 0; bottom: 0;
    height: 78px;
    background: var(--band-blue);
    display: flex;
    align-items: center;
    justify-content: center;
    color: var(--white);
    font-size: 19px;
    letter-spacing: .3px;
  }
</style>
</head>
<body>

<section class="card card--back">
  <div class="chief-logo">BRIGHTLANE CHIEF</div>
  <div class="person">
    <div class="person__name">Dorian Welker</div>
    <div class="person__title">The Brightlane Chief</div>
  </div>
  <div class="chief-rule"></div>

  <div class="contact-band">
    <div class="contact-cell">
      <svg class="contact-cell__icon" viewBox="0 0 34 34" aria-hidden="true">
        <circle cx="17" cy="17" r="15" fill="#fff" stroke="#8a8d8f" stroke-width="2"/>
        <rect x="12" y="9" width="10" height="16" rx="2" fill="none" stroke="#0a6fae" stroke-width="2"/>
        <line x1="15" y1="22" x2="19" y2="22" stroke="#0a6fae" stroke-width="1.6"/>
      </svg>
      555-204-3378
    </div>
    <div class="contact-cell">
      <svg class="contact-cell__icon" viewBox="0 0 34 34" aria-hidden="true">
        <circle cx="17" cy="17" r="15" fill="#fff" stroke="#8a8d8f" stroke-width="2"/>
        <rect x="9" y="11" width="16" height="12" fill="#0a6fae"/>
        <polyline points="9,11 17,18 25,11" fill="none" stroke="#fff" stroke-width="1.6"/>
      </svg>
      Dorian@BrightlaneChief.com
    </div>
    <div class="contact-cell">
      <svg class="contact-cell__icon" viewBox="0 0 34 34" aria-hidden="true">
        <circle cx="17" cy="17" r="15" fill="#fff" stroke="#8a8d8f" stroke-width="2"/>
        <rect x="8" y="13" width="11" height="8" rx="4" fill="none" stroke="#0a6fae" stroke-width="2.4"/>
        <rect x="15" y="13" width="11" height="8" rx="4" fill="none" stroke="#0a6fae" stroke-width="2.4"/>
      </svg>
      www.BrightlaneChief.com
    </div>
  </div>
</section>

<section class="card card--front">
  <div class="reach-logo">BRIGHTLANE REACH</div>
  <div class="reach-rule"></div>
  <div class="tagline">Every Bold Step Opens A Brighter Lane</div>
  <div class="web">www.<span class="web__name">BrightlaneReach</span>.com</div>
  <div class="address-band">247 E. Pelham Row, 5th Floor, San Diego CA 92384</div>
</section>

</body>
</html>
```